Personalized cards/stationery for a good friend

I'd like someone to design an image that could be used on stationery, specifically the front of a greeting/thank you type card. My friend is recently married and bought a house. I would like to use her preference towards traditional/preppy style (think Ravlo on a boat) with a silhouette of a woman, man and Corgi dog possibly with a beach or house in the background. I would like to incorporate their initials or monogram elegantly - RDK and BDK. Let me know if you have any questions or need additional input!

Target Market(s)

Female and Male, 35 yrs old, married w/house and dog

Font styles to use
Serif
Script

Requirements
Must have
• Initials/monogram (doesn't have to be all 3 letters, RK and BK is ok)
• Elegant, traditional, preppy
• include dog - corgi

```html
<!DOCTYPE html>
<html lang="en">
<head>
<meta charset="utf-8">
<title>R &amp; B Stationery — Card Concepts</title>
<link href="https://fonts.googleapis.com/css2?family=Great+Vibes&family=Roboto:wght@300&display=swap" rel="stylesheet">
<style>
  :root {
    --page: #e9e5df;
    --label: #8a8783;
    --red: #e8202a;
    --gold: #c89a4e;
    --gold-light: #f3dba4;
    --gold-dark: #9c7030;
    --navy: #1f3189;
    --pink: #e8157f;
    --pink-soft: #f48fb8;
    --stripe-white: #fbf6ea;
  }
  * { box-sizing: border-box; margin: 0; padding: 0; }
  html, body { width: 1200px; height: 1200px; overflow: hidden; }
  body { background: var(--page); position: relative; font-family: "Roboto", Arial, sans-serif; }

  .concept { position: absolute; width: 322px; }
  .concept-label { position: absolute; top: -46px; left: 0; font-size: 42px; font-weight: 300; color: var(--label); letter-spacing: -1px; }

  .card { position: relative; width: 322px; height: 462px; overflow: hidden; box-shadow: 0 3px 8px rgba(0,0,0,.25); }
  .card::after { content: ""; position: absolute; inset: 0 0 69px 0; pointer-events: none;
    background: repeating-linear-gradient(90deg, rgba(255,255,255,0) 0 5px, rgba(0,0,0,.10) 5px 7px, rgba(255,255,255,.12) 7px 9px); }
  .card.no-stripes::after { display: none; }

  .bg-rainbow { background: linear-gradient(180deg, #8e74c2 0%, #3fb2e8 18%, #5fcc6e 38%, #f7e632 58%, #f5a23a 72%); }
  .bg-pastel { background: linear-gradient(180deg, #4fc4ee 0%, #9aa6dc 40%, #e7a3cc 70%); }
  .bg-red { background: radial-gradient(ellipse 70% 70% at 50% 45%, #ec1c2a 60%, #f6a0a8 95%, #fde8ea 100%); }
  .bg-ocean { background: linear-gradient(180deg, #d84f9d 0%, #5b7fd0 16%, #08a8e6 38%, #1ba7e2 58%, #7a78c8 78%, #dd3fa0 100%); }

  .art { position: absolute; }
  .art-house { left: 0; top: 64px; width: 108px; height: 36px; border-radius: 4px 40px 4px 40px; }
  .art-couple { left: 80px; top: 40px; width: 170px; height: 300px; border-radius: 60px 60px 10px 10px; }
  .art-dog { left: 252px; top: 220px; width: 64px; height: 82px; border-radius: 28px 28px 8px 8px; }
  .tone-orange { background: linear-gradient(180deg, rgba(214,104,74,.75), rgba(224,110,60,.75)); }
  .tone-navy { background: #1f3189; }
  .tone-cream { background: linear-gradient(180deg, rgba(230,245,240,.85), rgba(252,240,200,.85)); }
  .tone-tan { background: linear-gradient(180deg, #c8a468, #d9bb86); }
  .tone-pink { background: var(--pink-soft); }

  .stripes-gold { position: absolute; left: 0; right: 0; top: 393px; bottom: 0;
    background: repeating-linear-gradient(90deg, var(--stripe-white) 0 6px, var(--gold) 6px 9px, var(--gold-light) 9px 11px); }

  .band { position: absolute; left: 0; right: 0; top: 323px; height: 70px; background: var(--red);
    border-top: 3px solid var(--gold); border-bottom: 3px solid var(--gold); }
  .band-navy { background: var(--navy); border-color: var(--pink); }
  .band-pink { background: linear-gradient(90deg, #e8157f, #f0306a 50%, #e8157f); }

  .seal { position: absolute; left: 77px; top: 274px; width: 168px; height: 168px; border-radius: 50%;
    background: var(--red); border: 6px solid var(--gold);
    box-shadow: inset 0 0 0 2px var(--gold-light), 0 2px 6px rgba(0,0,0,.35); }
  .seal-navy { background: var(--navy); border-color: var(--pink); box-shadow: inset 0 0 0 2px #f7a3cb; }

  .monogram { position: absolute; inset: 0; font-family: "Great Vibes", cursive; color: var(--gold-light);
    text-shadow: 0 1px 0 var(--gold-dark); }
  .monogram-pink { color: var(--pink); text-shadow: none; }
  .mono-first { position: absolute; left: 26px; top: 2px; font-size: 78px; line-height: 1; }
  .mono-amp { position: absolute; left: 82px; top: 32px; font-size: 34px; line-height: 1; }
  .mono-second { position: absolute; left: 54px; top: 56px; font-size: 82px; line-height: 1; }

  .c1 { left: 52px; top: 80px; } .c2 { left: 438px; top: 80px; } .c3 { left: 826px; top: 80px; }
  .c4 { left: 52px; top: 658px; } .c5 { left: 438px; top: 658px; } .c6 { left: 826px; top: 658px; }
</style>
</head>
<body>

<section class="concept c1">
  <span class="concept-label">1a</span>
  <div class="card bg-rainbow">
    <div class="art art-house tone-orange" role="img" aria-label="House on a hill silhouette"></div>
    <div class="art art-couple tone-orange" role="img" aria-label="Silhouette of a married couple"></div>
    <div class="art art-dog tone-orange" role="img" aria-label="Corgi dog silhouette"></div>
    <div class="stripes-gold"></div>
    <div class="band"></div>
    <div class="seal"><div class="monogram"><span class="mono-first">R</span><span class="mono-amp">&amp;</span><span class="mono-second">B</span></div></div>
  </div>
</section>

<section class="concept c2">
  <span class="concept-label">2a</span>
  <div class="card bg-rainbow">
    <div class="art art-house tone-navy" role="img" aria-label="House on a hill silhouette"></div>
    <div class="art art-couple tone-navy" role="img" aria-label="Silhouette of a married couple"></div>
    <div class="art art-dog tone-navy" role="img" aria-label="Corgi dog silhouette"></div>
    <div class="stripes-gold"></div>
    <div class="band"></div>
    <div class="seal"><div class="monogram"><span class="mono-first">R</span><span class="mono-amp">&amp;</span><span class="mono-second">B</span></div></div>
  </div>
</section>

<section class="concept c3">
  <span class="concept-label">3a</span>
  <div class="card bg-rainbow">
    <div class="art art-house tone-cream" role="img" aria-label="House on a hill silhouette"></div>
    <div class="art art-couple tone-cream" role="img" aria-label="Silhouette of a married couple"></div>
    <div class="art art-dog tone-cream" role="img" aria-label="Corgi dog silhouette"></div>
    <div class="stripes-gold"></div>
    <div class="band"></div>
    <div class="seal"><div class="monogram"><span class="mono-first">R</span><span class="mono-amp">&amp;</span><span class="mono-second">B</span></div></div>
  </div>
</section>

<section class="concept c4">
  <span class="concept-label">4a</span>
  <div class="card bg-pastel">
    <div class="art art-house tone-tan" role="img" aria-label="House on a hill silhouette"></div>
    <div class="art art-couple tone-tan" role="img" aria-label="Silhouette of a married couple"></div>
    <div class="art art-dog tone-tan" role="img" aria-label="Corgi dog silhouette"></div>
    <div class="stripes-gold"></div>
    <div class="band"></div>
    <div class="seal"><div class="monogram"><span class="mono-first">R</span><span class="mono-amp">&amp;</span><span class="mono-second">B</span></div></div>
  </div>
</section>

<section class="concept c5">
  <span class="concept-label">5a</span>
  <div class="card no-stripes bg-red">
    <div class="art art-house tone-pink" role="img" aria-label="House on a hill silhouette"></div>
    <div class="art art-couple tone-pink" role="img" aria-label="Silhouette of a married couple"></div>
    <div class="art art-dog tone-pink" role="img" aria-label="Corgi dog silhouette"></div>
    <div class="band band-navy"></div>
    <div class="seal seal-navy"><div class="monogram monogram-pink"><span class="mono-first">R</span><span class="mono-amp">&amp;</span><span class="mono-second">B</span></div></div>
  </div>
</section>

<section class="concept c6">
  <span class="concept-label">6a</span>
  <div class="card no-stripes bg-ocean">
    <div class="art art-house tone-navy" role="img" aria-label="House on a hill silhouette"></div>
    <div class="art art-couple tone-navy" role="img" aria-label="Silhouette of a married couple"></div>
    <div class="art art-dog tone-navy" role="img" aria-label="Corgi dog silhouette"></div>
    <div class="band band-pink"></div>
    <div class="seal"><div class="monogram"><span class="mono-first">R</span><span class="mono-amp">&amp;</span><span class="mono-second">B</span></div></div>
  </div>
</section>

</body>
</html>
```